Business Cards - Flexible and open for new ideas!

Ledger Willow is a service designed to assist both businesses and individuals in managing their paper receipts. We do this by scanning paper receipts and storing them as pdf files which are downloadable to access and view at any time. We extract the data from each receipt so it can also be downloaded in the form for TallyNest, Fundora, Excel, KRVZ or CSV. There is no need to manually do this anymore. Our site also offers various reporting and graphing functionalities to track and manage expenditures. Our goal is to take the stress and disorganization out of tax time and help businesses to receive as much deduction on their expenses over the year as possible.

I have created a logo which I like but comments and alternate logos are encouraged. I have included my PSD and Font file with the project. If you cant download them I can send them to you. Alternatively our current styling is viewable on our website at ledgerwillow-example.com.au.

(We are still open to new designs and colours and are happy to modify our logo/website etc. if you can recommend something better!)
Updates

Marguerite has cleared up the hexagon stack and we really like that if you could do this that would be great!. 

Warm regards,

Ledger Willow

On the back of the card we are really liking the large hexagon stack with no words either in the background or white overlaying the background. With the logo and the information to the side.

Due to the great responses we have now guaranteed the project!

The front of the card should have:

- Cleaned up hexagon stack with even spaces between the hexagons.
- Text same size and next to hexagon stack like in the logo
- The website on the front of the card
- The background to contain multiple hexagon stacks 

Back of the card:

- Contain the logo
- Use the hexagon stack as a background for part of the card (1/4 or 1/2)
- Space for address and 2 telephone numbers

Thanks for all that have posted designs so far!

Even thought we have the above current ideas, we are still open for any left field design. We can only comment on the above designs because we have seen them. If you have an idea or can create something that you think is great please feel free to submit it! 

Hey all.

We have had some fantastic designs and really would enjoy any final designs before the deadline this weekend.

If you have a totally unique idea please feel free to submit it even if you have already submitted something else.

If you feel you are unsure of what we want or we havent provided enough feedback please contact us and we can sort it out.

Target Market(s)

We are aiming for small to medium business owners, accountants and bookkeepers

Industry/Entity Type

Business

Requirements
Must have
• We would like to include our logo, which is navy blue for the hexagon stack and black for the title. Colours should include dark navy blues, lighters blues, black for other designs on the card.

We would like our web address, phone number and mailing address present; preferably be on the back of the business card, but feel free to wow us if you think you have a design but doesn't necessarily fit our guidelines :)
Should not have
• Dont like too much happening. Prefer simple and bold.

```html
<!DOCTYPE html>
<html lang="en">
<head>
<meta charset="utf-8">
<title>Ledger Willow Business Cards</title>
<link rel="stylesheet" href="https://fonts.googleapis.com/css2?family=Days+One&family=PT+Sans:wght@400;700&display=swap">
<style>
  :root {
    --stage: #e9eaec;
    --blue-deep: #0b4fa8;
    --blue-mid: #1a78d6;
    --blue-light: #3aa0f0;
    --grey-light: #f2f3f5;
    --grey-mid: #c9ccd3;
    --navy: #2b2a8c;
    --ink: #111317;
    --white: #ffffff;
    --white-soft: #dfeeff;
  }
  * { margin: 0; padding: 0; box-sizing: border-box; }
  html, body { width: 1200px; height: 951px; overflow: hidden; }
  body {
    background: var(--stage);
    position: relative;
    font-family: "PT Sans", Arial, sans-serif;
  }
  .card {
    position: absolute;
    width: 580px;
    height: 331px;
    border-radius: 4px;
    overflow: hidden;
    box-shadow: 0 6px 18px rgba(0,0,0,0.22);
  }
  .card-front { left: 110px; top: 100px; }
  .card-back { left: 510px; top: 520px; }

  .front-pattern {
    position: absolute; inset: 0;
    background: radial-gradient(ellipse at 45% 40%, var(--blue-light) 0%, var(--blue-mid) 45%, var(--blue-deep) 100%);
  }
  .brand {
    position: absolute;
    display: flex;
    align-items: center;
    gap: 16px;
  }
  .brand-mark {
    background: var(--navy);
    flex: none;
  }
  .brand-name {
    font-family: "Days One", "PT Sans", sans-serif;
    color: var(--ink);
    line-height: 1;
    white-space: nowrap;
  }
  .card-front .brand { left: 70px; top: 122px; }
  .card-front .brand-mark { width: 64px; height: 64px; }
  .card-front .brand-name { font-size: 46px; }
  .front-url {
    position: absolute;
    left: 70px; bottom: 40px;
    color: var(--white);
    font-size: 20px;
    letter-spacing: 0.5px;
  }

  .back-blue {
    position: absolute; inset: 0;
    background: linear-gradient(160deg, var(--blue-light) 0%, var(--blue-mid) 40%, var(--blue-deep) 100%);
  }
  .back-panel {
    position: absolute; top: 0; right: 0;
    width: 260px; height: 100%;
  }
  .back-panel svg { display: block; width: 100%; height: 100%; }
  .card-back .brand { right: 24px; top: 152px; gap: 10px; }
  .card-back .brand-mark { width: 34px; height: 34px; }
  .card-back .brand-name { font-size: 25px; }

  .person { position: absolute; left: 56px; top: 42px; color: var(--white); }
  .person-name { font-weight: 700; font-size: 20px; }
  .person-role { font-size: 14px; color: var(--white-soft); margin-top: 2px; }

  .contact-list {
    position: absolute; left: 28px; top: 128px;
    list-style: none; color: var(--white);
    font-size: 16px; line-height: 21px;
  }
  .contact-list li { display: flex; align-items: flex-start; gap: 10px; }
  .contact-list .address { margin-bottom: 14px; }
  .contact-icon { width: 14px; height: 14px; flex: none; margin-top: 3px; fill: var(--white); }
</style>
</head>
<body>

<section class="card card-front" aria-label="Business card front">
  <div class="front-pattern" role="img" aria-label="Blue background with faint repeating hexagon stack pattern"></div>
  <div class="brand">
    <span class="brand-mark"></span>
    <span class="brand-name">Ledger Willow</span>
  </div>
  <p class="front-url">www.ledgerwillow-example.com.au</p>
</section>

<section class="card card-back" aria-label="Business card back">
  <div class="back-blue"></div>
  <div class="back-panel">
    <svg viewBox="0 0 260 331" preserveAspectRatio="none" role="img" aria-label="Light grey panel with faint hexagon stack pattern">
      <defs>
        <linearGradient id="panelGrey" x1="0" y1="0" x2="1" y2="1">
          <stop offset="0" stop-color="#f7f8fa"/>
          <stop offset="1" stop-color="#c6c9d0"/>
        </linearGradient>
      </defs>
      <path d="M40 0 H260 V331 H10 C32 250 38 170 30 90 C27 55 30 25 40 0 Z" fill="#ffffff" opacity="0.7"/>
      <path d="M48 0 H260 V331 H20 C42 250 46 170 38 90 C35 55 38 25 48 0 Z" fill="url(#panelGrey)"/>
    </svg>
  </div>
  <div class="brand">
    <span class="brand-mark"></span>
    <span class="brand-name">Ledger Willow</span>
  </div>

  <div class="person">
    <p class="person-name">Owen Castellan</p>
    <p class="person-role">director</p>
  </div>

  <ul class="contact-list">
    <li class="address">
      <svg class="contact-icon" viewBox="0 0 14 14"><path d="M7 1 L13 7 H11 V13 H8.5 V9 H5.5 V13 H3 V7 H1 Z"/></svg>
      <span>P.O. Box 4417<br>Brookmere, WI 50310</span>
    </li>
    <li>
      <svg class="contact-icon" viewBox="0 0 14 14"><path d="M3 1 L5.5 1 L6.5 4 L5 5.3 C5.8 7 7 8.2 8.7 9 L10 7.5 L13 8.5 V11 C13 12 12 13 11 13 C6 12.5 1.5 8 1 3 C1 2 2 1 3 1 Z"/></svg>
      <span>555-0148-221</span>
    </li>
    <li>
      <svg class="contact-icon" viewBox="0 0 14 14"><circle cx="7" cy="7" r="6"/></svg>
      <span>555-0193-607</span>
    </li>
    <li>
      <svg class="contact-icon" viewBox="0 0 14 14"><circle cx="7" cy="7" r="5.5" fill="none" stroke="#fff" stroke-width="1.4"/><path d="M1.5 7 H12.5 M7 1.5 C4 4.5 4 9.5 7 12.5 M7 1.5 C10 4.5 10 9.5 7 12.5" fill="none" stroke="#fff" stroke-width="1.2"/></svg>
      <span>www.ledgerwillow-example.com.au</span>
    </li>
    <li>
      <svg class="contact-icon" viewBox="0 0 14 14"><path d="M1 3 H13 V11 H1 Z M1.5 3.5 L7 8 L12.5 3.5" fill="none" stroke="#fff" stroke-width="1.4"/></svg>
      <span>info@ledgerwillow-example.com.au</span>
    </li>
  </ul>
</section>

</body>
</html>
```